Trifold brochure

Need a trifold marketing brochure for my autism therapy for children business . I would be interested in having designs in both English and Spanish if possible!!!!! Website is www.quillmeadowtherapy.com
Address on brochure needs to be 2736 Larkspur Ave W Suite 5
Minneapolis, MN 55719
Updates
Can you update the address on brochure to 2736 Larkspur Ave W Suite 5
Minneapolis, MN 55719
Target Market(s)
Autism therapy for children
Industry/Entity Type
Autism Therapy
Look and feel

```html
<!DOCTYPE html>
<html lang="en">
<head>
<meta charset="utf-8">
<title>Quill Meadow Therapy – Trifold Brochure</title>
<link href="https://fonts.googleapis.com/css2?family=Lora:ital,wght@0,600;0,700;1,500;1,600&family=Poppins:ital,wght@0,400;0,500;0,600;0,700;1,400&display=swap" rel="stylesheet">
<style>
:root{
  --navy:#0f5696;
  --navy-bright:#1d6fba;
  --gold:#9a7331;
  --ink:#2b2b2b;
  --paper:#ffffff;
  --stage:#a9a9a9;
}
*{margin:0;padding:0;box-sizing:border-box}
html,body{width:803px;height:1200px;overflow:hidden;background:var(--stage)}
body{font-family:"Poppins",sans-serif;color:var(--ink);position:relative}
.spread{position:absolute;left:16px;width:771px;height:545px;background:var(--paper);overflow:hidden;box-shadow:0 2px 6px rgba(0,0,0,.25)}
.spread--outside{top:37px}
.spread--inside{top:618px}
.abs{position:absolute}
.layer{position:absolute;left:0;top:0}
.photo{position:absolute}
.body-text{font-size:6.3px;line-height:1.42}

/* outside spread */
.approach{left:0;top:0;width:257px;height:330px;background:var(--gold);color:#fff;padding:26px 16px 0 30px}
.approach h3{font-family:"Lora",serif;font-weight:600;font-size:10.5px;margin-bottom:14px}
.approach .intro{font-size:6.3px;line-height:1.45;margin-bottom:12px}
.approach .intro b{font-weight:700}
.feature{display:flex;gap:8px;margin-bottom:11px}
.tick-badge{flex:0 0 24px;height:24px;border-radius:50%;background:var(--navy);border:2px solid #fff;display:flex;align-items:center;justify-content:center}
.feature h4{font-family:"Lora",serif;font-weight:700;font-size:7.6px;margin-bottom:2px}
.feature p{font-size:5.8px;line-height:1.4}

.brand{text-align:center;color:var(--navy);font-family:"Poppins",sans-serif;font-weight:700;display:flex;align-items:center;justify-content:center;gap:6px}
.brand-dot{width:9px;height:9px;border-radius:50%;background:var(--navy);flex:0 0 auto}
.brand--large{left:257px;width:257px;top:118px;font-size:19px;line-height:1.05}
.brand--small{left:514px;width:257px;top:72px;font-size:15px;line-height:1.05}
.brand-rule{left:290px;width:190px;top:172px;height:1px;background:#d6c7ab}

.cta{left:257px;width:257px;top:203px;text-align:center}
.cta .eyebrow{font-family:"Lora",serif;font-style:italic;font-size:7.4px;color:#333;margin-bottom:5px}
.cta h2{font-family:"Lora",serif;font-weight:700;font-size:16.5px;line-height:1.15;color:var(--gold)}
.cta h2 span{color:var(--navy)}

.contact{left:275px;top:380px;width:220px;color:#fff}
.pill-gold{display:inline-block;background:var(--gold);color:#fff;font-weight:600;font-size:8.6px;padding:3px 11px;border-radius:10px;margin-bottom:12px;margin-left:12px}
.contact-row{display:flex;align-items:flex-start;gap:9px;font-size:9.4px;line-height:1.35;margin-bottom:11px}
.contact-row svg{flex:0 0 10px;margin-top:2px}
.social{display:flex;align-items:center;justify-content:center;gap:4px;margin-top:4px}
.social .line{width:52px;height:1px;background:#fff;margin:0 6px}
.social .dot{width:12px;height:12px;border-radius:50%;background:#fff}

.hero{left:514px;width:257px;top:390px;text-align:center;color:#fff}
.hero h1{font-family:"Lora",serif;font-weight:700;font-size:19.5px;line-height:1.12;margin-bottom:10px}
.hero p{font-size:7.4px;line-height:1.35;padding:0 16px;margin-bottom:13px}
.pill-navy{display:inline-block;background:var(--navy);color:#fff;font-family:"Lora",serif;font-weight:700;font-size:11px;padding:4px 18px;border-radius:12px}
.hero .pill-navy{background:var(--navy-bright)}

/* inside spread */
.about{left:28px;top:220px;width:212px}
.heading-navy{font-family:"Lora",serif;font-weight:700;color:var(--navy);font-size:10.8px;margin-bottom:4px}
.heading-rule{width:30px;height:2px;background:var(--gold);margin-bottom:12px}
.about .body-text{margin-bottom:22px}

.values{left:282px;top:24px;width:218px}
.values .kicker{font-family:"Lora",serif;font-style:italic;font-weight:500;color:var(--gold);font-size:9px}
.values h2{font-family:"Lora",serif;font-weight:700;color:var(--navy);font-size:11.4px;margin-bottom:4px}
.values .lead{margin-bottom:14px}
.value-row{display:flex;gap:10px;margin-bottom:14px}
.value-icon{flex:0 0 42px;height:42px;border-radius:50%;background:var(--gold);border:3px solid #fff;box-shadow:0 0 0 1px #e2d4ba;display:flex;align-items:center;justify-content:center}
.value-row h4{font-family:"Lora",serif;font-weight:700;font-size:8.6px;color:var(--gold)}
.values .pill-navy{display:block;text-align:center;width:212px;margin-top:8px;font-size:12px;padding:4px 0}

.services{left:514px;top:0;width:257px;height:400px;background:var(--navy);color:#fff;padding:24px 22px 0 22px}
.services h3{font-family:"Lora",serif;font-weight:700;font-size:11.5px;margin-bottom:3px}
.services .heading-rule{margin-bottom:10px}
.service{display:flex;gap:8px;margin-bottom:11px}
.service svg{flex:0 0 9px;margin-top:2px}
.service h4{font-family:"Lora",serif;font-weight:700;font-size:8.2px;line-height:1.2;margin-bottom:2px}
.service p{font-size:6.1px;line-height:1.4}
</style>
</head>
<body>

<section class="spread spread--outside" aria-label="Brochure outside spread">
  <svg class="layer" width="771" height="545" viewBox="0 0 771 545" aria-hidden="true">
    <path d="M0 330 C 240 300, 520 300, 771 360 L 771 372 C 520 318, 250 318, 0 352 Z" fill="var(--gold)"/>
    <path d="M0 352 C 250 318, 520 318, 771 372 L 771 378 C 520 326, 250 326, 0 358 Z" fill="#ffffff"/>
    <path d="M0 358 C 250 326, 520 326, 771 378 L 771 545 L 0 545 Z" fill="var(--navy)"/>
  </svg>

  <div class="abs approach">
    <h3>Our Approach</h3>
    <p class="intro">At Quill Meadow, we take a holistic approach to autism therapy, recognizing that each child is unique. Our services are tailored to address the specific needs of children with autism spectrum disorder (ASD). <b>Here’s what sets us apart:</b></p>
    <div class="feature">
      <span class="tick-badge"><svg width="11" height="9" viewBox="0 0 11 9"><path d="M1 4.5 L4 7.5 L10 1" fill="none" stroke="#fff" stroke-width="1.8"/></svg></span>
      <div><h4>Early Intervention</h4><p>Our programs focus on early detection, assessment, and intervention to maximize developmental gains during critical periods.</p></div>
    </div>
    <div class="feature">
      <span class="tick-badge"><svg width="11" height="9" viewBox="0 0 11 9"><path d="M1 4.5 L4 7.5 L10 1" fill="none" stroke="#fff" stroke-width="1.8"/></svg></span>
      <div><h4>Individualized Treatment Plans</h4><p>Our experienced therapists create personalized treatment plans based on each child’s strengths, challenges, and developmental goals.</p></div>
    </div>
    <div class="feature">
      <span class="tick-badge"><svg width="11" height="9" viewBox="0 0 11 9"><path d="M1 4.5 L4 7.5 L10 1" fill="none" stroke="#fff" stroke-width="1.8"/></svg></span>
      <div><h4>Safe and Supportive Environment</h4><p>Our therapy spaces are designed to be calming and sensory-friendly. We create a nurturing environment where children feel comfortable exploring and learning.</p></div>
    </div>
  </div>

  <div class="photo" role="img" aria-label="Photo of a smiling therapist and young boy sharing a laugh at a table" style="left:0;top:362px;width:257px;height:183px;background:linear-gradient(135deg,#c98f5e 0%,#e8c6a0 45%,#6d8fb5 100%)"></div>

  <div class="abs brand brand--large"><span class="brand-dot"></span><span>QUILL MEADOW<br>THERAPY</span></div>
  <div class="abs brand-rule"></div>

  <div class="abs cta">
    <p class="eyebrow">Ready to Take the Next Step?</p>
    <h2>Contact Us Today for <span>Expert Autism Therapy Services!</span></h2>
  </div>

  <div class="abs contact">
    <span class="pill-gold">Get In Touch</span>
    <div class="contact-row"><svg width="10" height="10" viewBox="0 0 10 10"><circle cx="5" cy="5" r="5" fill="#fff"/><path d="M3 2.6 L4.2 2.6 L4.6 4 L3.9 4.5 C4.3 5.4 4.8 5.9 5.6 6.2 L6.1 5.5 L7.4 5.9 L7.4 7.1 C5 7.3 2.8 5 3 2.6Z" fill="var(--navy)"/></svg><span>612-555-0148</span></div>
    <div class="contact-row"><svg width="10" height="12" viewBox="0 0 10 12"><path d="M5 0 C2.2 0 0.5 2 0.5 4.4 C0.5 7.4 5 12 5 12 C5 12 9.5 7.4 9.5 4.4 C9.5 2 7.8 0 5 0Z" fill="#fff"/><circle cx="5" cy="4.4" r="1.7" fill="var(--navy)"/></svg><span>2736 Larkspur Ave W Suite 5<br>Minneapolis, MN 55719</span></div>
    <div class="contact-row"><svg width="10" height="10" viewBox="0 0 10 10"><circle cx="5" cy="5" r="5" fill="#fff"/><rect x="2.3" y="3.2" width="5.4" height="3.8" fill="none" stroke="var(--navy)" stroke-width=".8"/><path d="M2.3 3.2 L5 5.3 L7.7 3.2" fill="none" stroke="var(--navy)" stroke-width=".8"/></svg><span>info@quillmeadowtherapy.com</span></div>
    <div class="contact-row"><svg width="10" height="10" viewBox="0 0 10 10"><circle cx="5" cy="5" r="5" fill="#fff"/><circle cx="5" cy="5" r="2.8" fill="none" stroke="var(--navy)" stroke-width=".7"/><path d="M2.2 5 H7.8 M5 2.2 C3.8 3.8 3.8 6.2 5 7.8 M5 2.2 C6.2 3.8 6.2 6.2 5 7.8" fill="none" stroke="var(--navy)" stroke-width=".6"/></svg><span>quillmeadowtherapy.com</span></div>
    <div class="social"><span class="line"></span><span class="dot"></span><span class="dot"></span><span class="dot"></span><span class="line"></span></div>
  </div>

  <div class="abs brand brand--small"><span class="brand-dot"></span><span>QUILL MEADOW<br>THERAPY</span></div>
  <div class="photo" role="img" aria-label="Photo of a teacher with glasses reading a book with a young boy at a desk" style="left:514px;top:150px;width:257px;height:195px;background:linear-gradient(160deg,#f2f2f2 0%,#e7d3c2 45%,#c9a07e 70%,#e9edf1 100%)"></div>

  <div class="abs hero">
    <h1>Building Bridges to<br>Brighter Futures</h1>
    <p>Discovering the Unique Potential of Every Child through Compassionate, Evidence-Based Autism Therapy, Fostering Growth, Connection, and Confidence.</p>
    <span class="pill-navy">quillmeadowtherapy.com</span>
  </div>
</section>

<section class="spread spread--inside" aria-label="Brochure inside spread">
  <div class="photo" role="img" aria-label="Photo of two little girls playing with colourful puzzle pieces at a table" style="left:0;top:0;width:257px;height:210px;background:linear-gradient(150deg,#e9e2dc 0%,#c79b7b 40%,#9ec25a 65%,#f0ece8 100%);border-radius:0 0 60% 0 / 0 0 18% 0"></div>
  <div class="photo" role="img" aria-label="Circular photo of a mother hugging her young son on a play mat" style="left:135px;top:122px;width:110px;height:110px;border-radius:50%;border:4px solid #fff;background:radial-gradient(circle at 45% 40%,#d7b49a 0%,#8a6d5a 55%,#6aa37a 100%)"></div>

  <div class="abs about">
    <h3 class="heading-navy">About ABA Therapy</h3>
    <div class="heading-rule"></div>
    <p class="body-text">ABA Therapy Applied Behavioral Analysis (ABA) Therapy is endorsed by the National Child Health Board and the Northstar Pediatric Council and has been scientifically proven to be the most effective in helping a child with autism to acquire the necessary skills to reach their full potential. Research has proven that early diagnosis and intervention are key to achieving success, as well as a commitment to the individualized treatment plan developed specifically for your child by one of our expert Clinicians.</p>
    <h3 class="heading-navy">How We Do ABA Therapy</h3>
    <div class="heading-rule"></div>
    <p class="body-text">Quill Meadow offers a safe and clean center-based environment, led by highly-trained clinicians. Our team of experienced Certified Behavior Specialists (CBS) and Licensed Behavior Aides work with you and your child to develop individualized treatment plans based on their unique needs.</p>
  </div>

  <div class="abs values">
    <p class="kicker">Our Value</p>
    <h2>Quality Care From Quality Experts.</h2>
    <div class="heading-rule"></div>
    <p class="body-text lead">At Quill Meadow, our values drive our mission. We provide compassionate, evidence-based therapy for children with autism, focusing on individualized care and early intervention in a nurturing environment.</p>
    <div class="value-row">
      <span class="value-icon"><svg width="22" height="14" viewBox="0 0 22 14"><path d="M1 7 C5 1 17 1 21 7 C17 13 5 13 1 7Z" fill="#fff"/><circle cx="11" cy="7" r="3.6" fill="var(--gold)"/><circle cx="11" cy="7" r="1.6" fill="#fff"/></svg></span>
      <div><h4>Vision</h4><p class="body-text">To envision and strive towards a future where every child diagnosed with autism is supported, empowered, and equipped to achieve their fullest potential, fostering inclusivity and acceptance.</p></div>
    </div>
    <div class="value-row">
      <span class="value-icon"><svg width="20" height="20" viewBox="0 0 20 20"><circle cx="10" cy="10" r="8" fill="none" stroke="#fff" stroke-width="1.6"/><circle cx="10" cy="10" r="4.6" fill="none" stroke="#fff" stroke-width="1.6"/><circle cx="10" cy="10" r="1.6" fill="#fff"/><path d="M10 10 L17 3" stroke="#fff" stroke-width="1.4"/></svg></span>
      <div><h4>Mission</h4><p class="body-text">We’re dedicated to providing personalized, evidence-based therapy for every child with autism. Through early intervention and compassionate care, we empower growth and confidence, fostering thriving futures.</p></div>
    </div>
    <div class="value-row">
      <span class="value-icon"><svg width="20" height="20" viewBox="0 0 20 20"><rect x="3" y="5" width="12" height="12" rx="1" fill="none" stroke="#fff" stroke-width="1.5"/><path d="M8 12 L17 3" stroke="#fff" stroke-width="2"/><path d="M6 10 H11 M6 13 H10" stroke="#fff" stroke-width="1"/></svg></span>
      <div><h4>Motto</h4><p class="body-text">Unlocking Potential, Building Bridges, Illuminating Futures: Together, We Build Brighter Tomorrows.</p></div>
    </div>
    <span class="pill-navy">quillmeadowtherapy.com</span>
  </div>

  <div class="abs services">
    <h3>Our Services</h3>
    <div class="heading-rule"></div>
    <div class="service"><svg width="9" height="8" viewBox="0 0 9 8"><path d="M1 4 L3.5 6.5 L8 1" fill="none" stroke="#fff" stroke-width="1.6"/></svg><div><h4>Applied Behavior Analysis (ABA) Therapy</h4><p>Our ABA therapy focuses on enhancing communication, social skills, and behavior management in children with autism spectrum disorder (ASD).</p></div></div>
    <div class="service"><svg width="9" height="8" viewBox="0 0 9 8"><path d="M1 4 L3.5 6.5 L8 1" fill="none" stroke="#fff" stroke-width="1.6"/></svg><div><h4>Speech and Language Therapy</h4><p>Our speech and language therapy services aim to improve communication, expressive language, and social interaction abilities in children with autism. Using tailored approaches and innovative techniques</p></div></div>
    <div class="service"><svg width="9" height="8" viewBox="0 0 9 8"><path d="M1 4 L3.5 6.5 L8 1" fill="none" stroke="#fff" stroke-width="1.6"/></svg><div><h4>Occupational Therapy (OT)</h4><p>Occupational therapy at Quill Meadow targets the development of fine motor skills, sensory processing abilities, and self-care capabilities in children with autism. Through engaging activities and individualized interventions, our occupational therapists help children build essential life skills and gain independence in daily activities.</p></div></div>
    <div class="service"><svg width="9" height="8" viewBox="0 0 9 8"><path d="M1 4 L3.5 6.5 L8 1" fill="none" stroke="#fff" stroke-width="1.6"/></svg><div><h4>Social Skills Training</h4><p>Our social skills training programs focus on teaching crucial social skills to children with autism, enabling them to navigate social interactions confidently. Through structured group activities and personalized coaching.</p></div></div>
  </div>

  <svg class="layer" width="771" height="545" viewBox="0 0 771 545" aria-hidden="true">
    <path d="M257 420 C 420 350, 620 345, 771 372 L 771 386 C 620 360, 420 366, 257 432 Z" fill="var(--gold)"/>
  </svg>
  <div class="photo" role="img" aria-label="Photo of children's hands holding up colourful puzzle pieces against a bright sky" style="left:257px;top:0;width:514px;height:545px;clip-path:path('M0 434 C 163 368, 363 362, 514 388 L 514 545 L 0 545 Z');background:linear-gradient(100deg,#cfdcec 0%,#eef3f8 40%,#d9e3ee 70%,#b7c8dc 100%)"></div>
</section>

</body>
</html>
```